Bluefen Camper Hire Club (motorhome) rental club needs a web desin

The name of our club is Bluefen Camper Hire Club. I am looking for a web site that will show our motorhomes.
It needs to let us add motorhomes and change descriptions etc. (back end functionality)
It needs to show an RV with a description, with a calendar of availability for each RV.
It needs to allow club members the ability to schedule and pay for an RV. (ecommerce)
It needs a page where new members can go to join the club.
check out this link for an idea of how I would like the RVs presented. http://www.dorvalewingschool.example/Aircraft.html
We are an RV (motor home) rental club. Bluefencamperhireclub.com.
Needed is one cohesive design which will be used for more than 1 page. I need the web site to:
1. show our RV's for rent.
It must show a picture with details about the RV, (image placeholder for now – can possible give picture with details about the RV later on to the winning designer)
....with a link to the calendar for that RV which must allow a club member to pick the dates they want (the calendar must block them from picking dates that have been reserved or are less than the minimum days allowed for that time period (3 days low season and 5 days high season) the amounts for this must be changeable by us, a dollar amount for each day, week or month. This they will put in their shopping cart which must calculate a total and allow them to delete items. It also must allow them to put down a deposit if more than 30 days out or
pay 100% if under 30 days. There needs to be a link to extras they can add to the cart such as linens, kitchenware, delivery service, pickup service, dump charge, fuel charge, propane charge etc. This is a separate page good for all Rv's There needs to be a link to more pictures.
2. There needs to be a members area that they can log into with a user name
and a password that show their passed rentals and up coming rentals.
3 There needs to be a new members area that allows them to input their information, name, address, credit card, etc., agree to the rules of the club. This is where they will create there user name a password.
4. There needs to be an administrator area that shows a list of the RVs a
calendar for each with the dates that are taken. The area needs to show the
deposits received the rents received, there needs to be a reports area the
will show revenue received by dates picked. It needs to let's us take the
RV offline for repairs Etc. (back end)
5. Needs to be away to track sales tax. (This could be part of the reports
area)
6. There needs to be a "how it works tab".
7. An “about us” tab.
8. There needs to be a way to add new RVs and make other changes as needed. (back end)
Thanks, Lou Barnes

```html
<!DOCTYPE html>
<html lang="en">
<head>
<meta charset="utf-8">
<title>Bluefen Camper Hire Club</title>
<link href="https://fonts.googleapis.com/css2?family=Raleway:wght@400;500;600;700&family=Open+Sans:wght@400;600;700&display=swap" rel="stylesheet">
<style>
:root{
  --bg:#0b0b0b;
  --nav:#121212;
  --panel:#1b1b1b;
  --red:#d50d12;
  --white:#ffffff;
  --text:#d8d8d8;
  --dim:#5c5c5c;
}
*{box-sizing:border-box;margin:0;padding:0}
html,body{width:690px;height:1200px;overflow:hidden;background:var(--bg)}
body{position:relative;font-family:"Open Sans",sans-serif;color:var(--text)}
.abs{position:absolute}
.header{left:0;top:0;width:690px;height:52px;background:var(--bg)}
.brand{left:57px;top:16px;font-family:"Raleway",sans-serif;font-size:15px;font-weight:500;color:var(--white);white-space:nowrap}
.call{right:57px;top:14px;text-align:right}
.call small{display:block;font-size:5.5px;font-weight:700;color:var(--white);margin-right:20px}
.call span{display:block;font-size:8.5px;font-weight:700;color:var(--red);letter-spacing:.5px;margin-right:20px;margin-top:2px}
.call .dot{position:absolute;right:0;top:3px;width:15px;height:15px;border:1.5px solid var(--white);border-radius:50%}
.nav{left:0;top:52px;width:690px;height:25px;background:var(--nav)}
.nav ul{list-style:none;position:absolute;left:67px;top:7px;display:flex}
.nav li{font-family:"Raleway",sans-serif;font-size:8px;color:var(--white);margin-right:18.5px;white-space:nowrap}
.social{right:59px;top:6px;display:flex;gap:3px}
.social i{display:block;width:13px;height:13px;border:1px solid #cfcfcf;border-radius:50%}
.hero{left:0;top:77px;width:690px;height:228px;background:linear-gradient(180deg,#7d8b8a 0%,#5d6d6a 35%,#3f5149 60%,#545453 85%,#3a3a3a 100%)}
.join{left:98px;top:99px;width:141px;height:183px;background:rgba(30,30,30,.88);padding:14px 15px}
.join h2{font-family:"Raleway",sans-serif;font-size:11.5px;font-weight:700;color:var(--white);line-height:14px;margin-bottom:8px}
.join .field{height:19px;background:var(--white);margin-bottom:6px;font-size:5.5px;color:#9a9a9a;padding:6px 9px;letter-spacing:.3px}
.join .btn{height:18px;background:var(--red);color:var(--white);font-size:7.5px;font-weight:600;text-align:center;line-height:18px;margin-top:2px;font-family:"Raleway",sans-serif}
.tab{left:667px;top:121px;width:23px;height:105px;background:var(--red)}
.tab span{position:absolute;left:4px;top:75px;transform:rotate(-90deg);transform-origin:left top;font-family:"Raleway",sans-serif;font-size:10px;color:var(--white);white-space:nowrap;width:70px}
.listings{left:0;top:305px;width:690px;height:732px;background:linear-gradient(180deg,#171717 0%,#0c0c0c 60%,#080808 100%)}
.section-title{left:57px;top:318px;font-family:"Raleway",sans-serif;font-size:12px;font-weight:400;color:var(--white)}
.search{left:547px;top:321px;width:85px;height:16px;background:#2b2b2b;font-size:5.5px;color:#bbb;padding:5px 6px}
.search svg{position:absolute;right:6px;top:4px}
.card{left:57px;width:577px;height:146px;background:var(--panel)}
.card .photo{position:absolute;left:0;top:0;width:255px;height:146px;background:radial-gradient(ellipse at 50% 55%,#d9d9d9 0%,#9a9a9a 30%,#1a1a1a 58%,#111 100%)}
.card h3{position:absolute;left:269px;top:17px;font-family:"Raleway",sans-serif;font-size:8.5px;font-weight:400;color:var(--white);letter-spacing:.2px;white-space:nowrap}
.card p{position:absolute;left:269px;top:33px;width:292px;font-size:6.2px;line-height:8.3px;color:#bdbdbd}
.specs{position:absolute;top:67px;font-size:5.6px;line-height:15.3px;color:var(--dim);white-space:nowrap}
.specs.left{left:270px}
.specs.right{left:409px}
.specs div{display:flex}
.specs.left .k{width:36px}
.specs.left .d{width:15px}
.specs.right .k{width:30px}
.specs.right .d{width:30px}
.specs .h{color:var(--white);font-weight:700;font-family:"Raleway",sans-serif}
.actions{position:absolute;left:524px;top:65px}
.actions .ib{width:22px;height:19px;background:var(--white);margin-bottom:3.5px;display:flex;align-items:center;justify-content:center}
.actions .ib.red{background:var(--red)}
.booknow{position:absolute;left:546px;top:69px;width:31px;height:10px;background:var(--red);color:var(--white);font-size:5.3px;line-height:10px;text-align:center}
.cta{left:265px;top:989px;width:160px;height:27px;background:var(--red);color:var(--white);font-family:"Raleway",sans-serif;font-size:9px;text-align:center;line-height:27px}
.footer{left:0;top:1037px;width:690px;height:135px;background:#111}
.fcol{top:1046px}
.fcol h4{font-family:"Raleway",sans-serif;font-size:11px;font-weight:400;color:#3a3a3a;line-height:16px}
.fcol h4 b{display:block;font-weight:400;color:#6a6a6a}
.fcol h4 b em{font-style:normal;font-weight:700;color:#6a6a6a}
.fcol .copy{font-size:6px;line-height:8.6px;color:#b0b0b0;margin-top:10px;width:138px}
.news .row{display:flex;margin-top:10px}
.news .name{width:91px;height:23px;background:var(--white);font-size:6px;color:#666;padding:8px 9px}
.news .sub{width:46px;height:23px;background:var(--red);color:var(--white);font-size:6px;font-weight:600;line-height:23px;text-align:center}
.news .copy{width:130px}
.contact ul{list-style:none;margin-top:10px}
.contact li{position:relative;padding-left:15px;font-size:6.8px;line-height:11.5px;color:#bdbdbd;margin-bottom:6px}
.contact li svg{position:absolute;left:0;top:2px}
.bottom{left:0;top:1172px;width:690px;height:28px;background:#050505;font-size:5.5px;color:#d0d0d0;text-align:center;line-height:28px}
.bottom span{position:absolute;right:55px;top:0;font-size:5.5px}
</style>
</head>
<body>

<header class="abs header">
  <div class="abs brand">Bluefen Camper Hire Club</div>
  <div class="abs call">
    <small>Call Us Now</small>
    <span>55 018 4471</span>
    <i class="dot"></i>
  </div>
</header>

<nav class="abs nav">
  <ul>
    <li>Home</li><li>Motor Homes</li><li>Bluefen RV's</li><li>Book now</li><li>About Us</li><li>Contact Us</li><li>Member Login</li><li>Join The Club</li>
  </ul>
  <div class="abs social"><i></i><i></i><i></i><i></i><i></i></div>
</nav>

<section class="abs hero" role="img" aria-label="Photo of motorhomes parked on a rocky lakeshore below misty green mountains"></section>

<form class="abs join">
  <h2>Temporibus autem quibusdam</h2>
  <div class="field">NAME</div>
  <div class="field">EMAIL</div>
  <div class="field">PHONE</div>
  <div class="field">CITY</div>
  <div class="btn">JOIN THE CLUB</div>
</form>

<div class="abs tab"><span>Instructions</span></div>

<section class="abs listings"></section>
<h1 class="abs section-title">OUR BLUEFEN RV LISTINGS</h1>
<div class="abs search">SEARCH
  <svg width="8" height="8" viewBox="0 0 8 8"><circle cx="3.2" cy="3.2" r="2.4" fill="none" stroke="#bbb" stroke-width="1"/><line x1="5" y1="5" x2="7.5" y2="7.5" stroke="#bbb" stroke-width="1.2"/></svg>
</div>

<article class="abs card" style="top:347px">
  <div class="photo" role="img" aria-label="Photo of a white motorhome"></div>
  <h3>NEQUE PORRO QUISQUAM EST, QUI DOLOREM IPSUM</h3>
  <p>Sed ut perspiciatis unde omnis iste natus error sit voluptatem accusantium doloremque laudantium, totam rem aperiam, eaque ipsa quae ab illo inventore veritatis et quasi architecto beatae vitae dicta sunt explicabo.</p>
  <div class="specs left"><div><span class="k">Make</span><span class="d">—</span>Corvane</div><div><span class="k">Model</span><span class="d">—</span>K24</div><div><span class="k">Seats</span><span class="d">—</span>16</div><div><span class="k">Engine</span><span class="d">—</span>160 HP Tarrow</div></div>
  <div class="specs right"><div class="h">AVIONICS AND FEATURES</div><div><span class="k">Avionics</span><span class="d">—</span>Velnor VX 430</div><div><span class="k">Certified</span><span class="d">—</span>IFR</div><div><span class="k">Traffic</span><span class="d">—</span>n/a</div></div>
  <div class="actions">
    <div class="ib red"><svg width="10" height="10" viewBox="0 0 10 10"><rect x="1" y="2" width="6" height="7" fill="none" stroke="#fff"/><line x1="4" y1="6" x2="9" y2="1" stroke="#fff" stroke-width="1.3"/></svg></div>
    <div class="ib"><svg width="10" height="10" viewBox="0 0 10 10"><rect x="1" y="4" width="5" height="3" rx="1.5" fill="none" stroke="#111" stroke-width="1.3" transform="rotate(-45 3.5 5.5)"/><rect x="4" y="3" width="5" height="3" rx="1.5" fill="none" stroke="#111" stroke-width="1.3" transform="rotate(-45 6.5 4.5)"/></svg></div>
    <div class="ib"><svg width="10" height="10" viewBox="0 0 10 10"><rect x="1" y="2" width="8" height="7" fill="none" stroke="#111"/><line x1="1" y1="4" x2="9" y2="4" stroke="#111"/><line x1="3" y1="1" x2="3" y2="3" stroke="#111"/><line x1="7" y1="1" x2="7" y2="3" stroke="#111"/></svg></div>
  </div>
  <div class="booknow">Book now</div>
</article>

<article class="abs card" style="top:506px">
  <div class="photo" role="img" aria-label="Photo of a white coach-style motorhome"></div>
  <h3>NEQUE PORRO QUISQUAM EST, QUI DOLOREM IPSUM</h3>
  <p>Sed ut perspiciatis unde omnis iste natus error sit voluptatem accusantium doloremque laudantium, totam rem aperiam, eaque ipsa quae ab illo inventore veritatis et quasi architecto beatae vitae dicta sunt explicabo.</p>
  <div class="specs left"><div><span class="k">Make</span><span class="d">—</span>Corvane</div><div><span class="k">Model</span><span class="d">—</span>K24</div><div><span class="k">Seats</span><span class="d">—</span>16</div><div><span class="k">Engine</span><span class="d">—</span>160 HP Tarrow</div></div>
  <div class="specs right"><div class="h">AVIONICS AND FEATURES</div><div><span class="k">Avionics</span><span class="d">—</span>Velnor VX 430</div><div><span class="k">Certified</span><span class="d">—</span>IFR</div><div><span class="k">Traffic</span><span class="d">—</span>n/a</div></div>
  <div class="actions">
    <div class="ib red"><svg width="10" height="10" viewBox="0 0 10 10"><rect x="1" y="2" width="6" height="7" fill="none" stroke="#fff"/><line x1="4" y1="6" x2="9" y2="1" stroke="#fff" stroke-width="1.3"/></svg></div>
    <div class="ib"><svg width="10" height="10" viewBox="0 0 10 10"><rect x="1" y="4" width="5" height="3" rx="1.5" fill="none" stroke="#111" stroke-width="1.3" transform="rotate(-45 3.5 5.5)"/><rect x="4" y="3" width="5" height="3" rx="1.5" fill="none" stroke="#111" stroke-width="1.3" transform="rotate(-45 6.5 4.5)"/></svg></div>
    <div class="ib"><svg width="10" height="10" viewBox="0 0 10 10"><rect x="1" y="2" width="8" height="7" fill="none" stroke="#111"/><line x1="1" y1="4" x2="9" y2="4" stroke="#111"/><line x1="3" y1="1" x2="3" y2="3" stroke="#111"/><line x1="7" y1="1" x2="7" y2="3" stroke="#111"/></svg></div>
  </div>
  <div class="booknow">Book now</div>
</article>

<article class="abs card" style="top:665px">
  <div class="photo" role="img" aria-label="Photo of a large silver class A motorhome"></div>
  <h3>NEQUE PORRO QUISQUAM EST, QUI DOLOREM IPSUM</h3>
  <p>Sed ut perspiciatis unde omnis iste natus error sit voluptatem accusantium doloremque laudantium, totam rem aperiam, eaque ipsa quae ab illo inventore veritatis et quasi architecto beatae vitae dicta sunt explicabo.</p>
  <div class="specs left"><div><span class="k">Make</span><span class="d">—</span>Corvane</div><div><span class="k">Model</span><span class="d">—</span>K24</div><div><span class="k">Seats</span><span class="d">—</span>16</div><div><span class="k">Engine</span><span class="d">—</span>160 HP Tarrow</div></div>
  <div class="specs right"><div class="h">AVIONICS AND FEATURES</div><div><span class="k">Avionics</span><span class="d">—</span>Velnor VX 430</div><div><span class="k">Certified</span><span class="d">—</span>IFR</div><div><span class="k">Traffic</span><span class="d">—</span>n/a</div></div>
  <div class="actions">
    <div class="ib red"><svg width="10" height="10" viewBox="0 0 10 10"><rect x="1" y="2" width="6" height="7" fill="none" stroke="#fff"/><line x1="4" y1="6" x2="9" y2="1" stroke="#fff" stroke-width="1.3"/></svg></div>
    <div class="ib"><svg width="10" height="10" viewBox="0 0 10 10"><rect x="1" y="4" width="5" height="3" rx="1.5" fill="none" stroke="#111" stroke-width="1.3" transform="rotate(-45 3.5 5.5)"/><rect x="4" y="3" width="5" height="3" rx="1.5" fill="none" stroke="#111" stroke-width="1.3" transform="rotate(-45 6.5 4.5)"/></svg></div>
    <div class="ib"><svg width="10" height="10" viewBox="0 0 10 10"><rect x="1" y="2" width="8" height="7" fill="none" stroke="#111"/><line x1="1" y1="4" x2="9" y2="4" stroke="#111"/><line x1="3" y1="1" x2="3" y2="3" stroke="#111"/><line x1="7" y1="1" x2="7" y2="3" stroke="#111"/></svg></div>
  </div>
  <div class="booknow">Book now</div>
</article>

<article class="abs card" style="top:823px">
  <div class="photo" role="img" aria-label="Photo of a white camper van with overcab bed"></div>
  <h3>NEQUE PORRO QUISQUAM EST, QUI DOLOREM IPSUM</h3>
  <p>Sed ut perspiciatis unde omnis iste natus error sit voluptatem accusantium doloremque laudantium, totam rem aperiam, eaque ipsa quae ab illo inventore veritatis et quasi architecto beatae vitae dicta sunt explicabo.</p>
  <div class="specs left"><div><span class="k">Make</span><span class="d">—</span>Corvane</div><div><span class="k">Model</span><span class="d">—</span>K24</div><div><span class="k">Seats</span><span class="d">—</span>16</div><div><span class="k">Engine</span><span class="d">—</span>160 HP Tarrow</div></div>
  <div class="specs right"><div class="h">AVIONICS AND FEATURES</div><div><span class="k">Avionics</span><span class="d">—</span>Velnor VX 430</div><div><span class="k">Certified</span><span class="d">—</span>IFR</div><div><span class="k">Traffic</span><span class="d">—</span>n/a</div></div>
  <div class="actions">
    <div class="ib red"><svg width="10" height="10" viewBox="0 0 10 10"><rect x="1" y="2" width="6" height="7" fill="none" stroke="#fff"/><line x1="4" y1="6" x2="9" y2="1" stroke="#fff" stroke-width="1.3"/></svg></div>
    <div class="ib"><svg width="10" height="10" viewBox="0 0 10 10"><rect x="1" y="4" width="5" height="3" rx="1.5" fill="none" stroke="#111" stroke-width="1.3" transform="rotate(-45 3.5 5.5)"/><rect x="4" y="3" width="5" height="3" rx="1.5" fill="none" stroke="#111" stroke-width="1.3" transform="rotate(-45 6.5 4.5)"/></svg></div>
    <div class="ib"><svg width="10" height="10" viewBox="0 0 10 10"><rect x="1" y="2" width="8" height="7" fill="none" stroke="#111"/><line x1="1" y1="4" x2="9" y2="4" stroke="#111"/><line x1="3" y1="1" x2="3" y2="3" stroke="#111"/><line x1="7" y1="1" x2="7" y2="3" stroke="#111"/></svg></div>
  </div>
  <div class="booknow">Book now</div>
</article>

<div class="abs cta">Click here for Schedule and Pay</div>

<footer class="abs footer"></footer>

<div class="abs fcol" style="left:66px">
  <h4>Welcome To<b>Bluefen Camper <em>Hire Club</em></b></h4>
  <div class="copy">Nam libero tempore, cum soluta nobis est eligendi optio cumque nihil impedit quo minus id quod maxime placeat facere possimus, omnis voluptas assumenda est, omnis dolor repellendus. Temporibus autem quibusdam et aut officiis debitis aut rerum necessitatibus saepe eveniet ut et voluptates repudiandae sint et molestiae non recusandae.</div>
</div>

<div class="abs fcol news" style="left:276px">
  <h4>Newsletter<b>Bluefen Camper <em>Hire Club</em></b></h4>
  <div class="row"><div class="name">Enter Name</div><div class="sub">SUBSCRIBE</div></div>
  <div class="copy">Excepteur sint occaecat cupidatat non proident, sunt in culpa qui</div>
</div>

<div class="abs fcol contact" style="left:486px">
  <h4>Contact Us</h4>
  <ul>
    <li><svg width="8" height="9" viewBox="0 0 8 9"><path d="M4 8.5C2 6 1 4.6 1 3.4a3 3 0 0 1 6 0C7 4.6 6 6 4 8.5z" fill="none" stroke="#9a9a9a"/><circle cx="4" cy="3.4" r="1" fill="#9a9a9a"/></svg>Main Store 48 Marlow Road<br>Fenbridge</li>
    <li><svg width="8" height="8" viewBox="0 0 8 8"><path d="M1.5 0.8l1.5 1.7-0.8 1c0.5 1 1.2 1.7 2.2 2.2l1-0.8 1.7 1.5-0.9 1.2C3.5 7.5 0.5 4.5 0.3 1.7z" fill="#9a9a9a"/></svg>55120 (555)-014-2290</li>
    <li><svg width="8" height="7" viewBox="0 0 8 7"><rect x="0.5" y="1" width="7" height="5" fill="#9a9a9a"/><path d="M0.5 1l3.5 3 3.5-3" fill="none" stroke="#111" stroke-width="0.8"/></svg>info@bluefencamperhireclub.com</li>
  </ul>
</div>

<div class="abs bottom">All Rights Reserved. Copyrights @ 2016 company name<span>M1</span></div>

</body>
</html>
```